Online interactive calendar for training organisation

We have a new website being made and need a design for an online calendar that is interactive and very simple and easy to use. On our main page this calendar will include all of our courses (approx 30 different ones with up to 8 different locations). On our sub pages which have course information, the calendar will only include details of that specific course. Details needed are: Course code, course name/title, date, duration (1/2 day - 5 days), location, price, discount price. Maybe also a key for available or limited spots left? We want a section at the top of the calendar to be able to filter by location or course, and maybe to filter by month also? I have included a spreadsheet with a sample of our courses with this information. Also a sample draft of the main page on our new webpage to show the colour green which is our company colour. Main notes - we want as simple, effective and easy to use as possible.
We will need to know what plug in we can use to get the design you have created.

Target Market(s)

Mining and construction - both companies and individuals

Number of Pages Required

1 page

Colors
cadf82

Requirements
Must have
• Be simple, easy to use, effective.

```html
<!DOCTYPE html>
<html lang="en">
<head>
<meta charset="utf-8">
<title>Course Calendar – Trackline Safety</title>
<link href="https://fonts.googleapis.com/css2?family=Montserrat:wght@400;500;600;700&family=Hind:wght@400;500;600&display=swap" rel="stylesheet">
<style>
:root{
  --brand:#cadf82;
  --bar:#9cc93b;
  --ink:#1b1b1b;
  --muted:#6a6a6a;
  --line:#555;
  --footer:#2b2b2b;
  --red:#d8201d;
  --cellgrey:#efefef;
  --head-grey:#e6e6e6;
}
*{box-sizing:border-box;margin:0;padding:0}
html,body{width:1200px;height:1034px;overflow:hidden;background:#fff;font-family:"Montserrat",sans-serif;color:var(--ink)}
.page{position:relative;width:1200px;height:1034px}
.abs{position:absolute}

.topbar{left:0;top:0;width:1200px;height:30px;background:var(--bar)}
.social{display:flex;gap:5px;left:226px;top:6px}
.social span{width:18px;height:18px;border-radius:50%;background:#1e1e1e;display:block}
.student{left:782px;top:5px;width:83px;height:20px;background:#2a2a2a;color:#fff;font:600 9px "Hind",sans-serif;display:flex;align-items:center;justify-content:center;border-radius:2px}
.search{left:872px;top:5px;width:106px;height:20px;background:#fff;border-radius:2px}
.search svg{position:absolute;right:7px;top:5px}

.brandmark{left:228px;top:48px;display:flex;align-items:center;gap:10px}
.brandmark i{width:40px;height:40px;border-radius:50%;background:var(--red);display:block}
.brandmark b{font:700 22px "Montserrat",sans-serif;color:var(--red);letter-spacing:.5px}

.nav{display:flex;gap:17px;font:400 9.6px "Hind",sans-serif;color:#333}
.nav .on{color:var(--bar)}
.nav.main{left:619px;top:59px}

.btn{background:var(--brand);border:1px solid #7f8f4a;display:flex;align-items:center;font:600 14px "Montserrat",sans-serif;color:var(--ink)}
.caret{width:0;height:0;border-left:4px solid transparent;border-right:4px solid transparent;border-top:5px solid var(--ink);position:absolute}
.month{left:188px;top:141px;width:131px;height:39px;padding-left:24px}
.month .caret{right:9px;top:17px}
.title{left:400px;top:136px;width:400px;text-align:center;font:600 36px "Montserrat",sans-serif;letter-spacing:1px}
.today{left:843px;top:141px;width:88px;height:39px;justify-content:center}
.arrows{left:945px;top:141px;width:68px;height:39px}
.arrows span{flex:1;height:100%;display:flex;align-items:center;justify-content:center}
.arrows span+span{border-left:1px solid #7f8f4a}

.goto{left:407px;top:210px;width:386px;height:38px}
.goto > div{position:relative;height:100%;display:flex;align-items:center;justify-content:center}
.goto > div+div{border-left:1px solid #7f8f4a}
.goto .y{width:87px;padding-right:12px}
.goto .m{width:136px;padding-right:14px}
.goto .g{flex:1}
.goto .caret{right:8px;top:17px}

.card{left:161px;top:308px;width:878px;height:442px;background:#fff;box-shadow:0 0 6px rgba(0,0,0,.28)}

.mini{width:100px}
.mini .lbl{text-align:center;font:500 5px "Montserrat",sans-serif;color:#9bb34f;line-height:6px}
.mini .yr{text-align:center;font:600 4px "Montserrat",sans-serif;line-height:6px}
.mini .hd{height:5px;background:var(--brand);margin-top:3px}
.mini .bd{height:56px;background:
  repeating-linear-gradient(90deg,#ddd 0 1px,transparent 1px 14.28px),
  repeating-linear-gradient(180deg,#ddd 0 1px,transparent 1px 9.3px)}

.monthhead{left:368px;top:344px;width:154px;text-align:center}
.monthhead .n{font:400 14px "Montserrat",sans-serif;letter-spacing:2px;border-bottom:1px solid #333;padding-bottom:1px}
.monthhead .nm{font:500 27px "Montserrat",sans-serif;color:var(--brand);line-height:36px;border-bottom:1px solid #333}
.monthhead .yr{font:400 20px "Montserrat",sans-serif;letter-spacing:1px;line-height:28px}

.weekdays{left:213px;top:440px;display:flex;gap:3px}
.weekdays span{width:63px;height:29px;background:var(--head-grey);display:flex;align-items:center;justify-content:center;font:500 8.5px "Montserrat",sans-serif}
.weekdays .we{background:var(--brand);color:#fff}

.grid{left:211px;top:475px;width:460px;display:grid;grid-template-columns:repeat(7,1fr);border-left:1px solid var(--line);border-top:1px solid var(--line)}
.grid span{height:47.8px;border-right:1px solid var(--line);border-bottom:1px solid var(--line);display:flex;align-items:flex-end;justify-content:flex-end;padding:0 5px 3px 0;font:500 9.5px "Montserrat",sans-serif}
.grid .prev{background:var(--cellgrey);color:#999;border-color:#fff;border-bottom-color:var(--line)}
.grid .sat{color:var(--brand)}
.grid .sel{background:var(--brand)}

.dtitle{left:749px;top:379px;width:250px;text-align:center;font:500 16px "Montserrat",sans-serif;color:var(--brand)}
.dline{left:817px;top:405px;width:113px;height:1px;background:#222}
.details{left:749px;top:417px;width:250px;height:297px;border:1px solid #444;padding:14px 26px}
.details dt{font:600 10.5px "Montserrat",sans-serif;margin-top:7px}
.details dt:first-child{margin-top:0}
.details dd{font:400 9px "Montserrat",sans-serif;color:var(--muted);margin-top:3px}

.footer{left:0;top:821px;width:1200px;height:174px;background:var(--footer)}
.fbrand{left:228px;top:870px;display:flex;align-items:center;gap:10px}
.fbrand i{width:40px;height:40px;border-radius:50%;background:var(--red);display:block}
.fbrand b{font:700 20px "Montserrat",sans-serif;color:var(--red)}
.follow{left:270px;top:920px;display:flex;align-items:center;gap:5px;font:400 12px "Hind",sans-serif;color:#ccc}
.follow span{width:19px;height:19px;background:#111;display:block}
.follow em{font-style:normal;margin-right:2px}
.nav.foot{left:619px;top:884px;color:#ddd}
.contact{top:922px;display:flex;align-items:center;gap:11px;font:400 11px "Hind",sans-serif;color:#ddd}
.contact .ic{width:24px;height:24px;background:#111;display:flex;align-items:center;justify-content:center}
.c1{left:589px}.c2{left:828px}
.bottombar{left:0;top:995px;width:1200px;height:39px;background:var(--bar);display:flex;align-items:center;justify-content:center;font:400 9.5px "Hind",sans-serif;color:#333}
.totop{left:1009px;top:972px;width:36px;height:37px;background:#fff;display:flex;align-items:center;justify-content:center;box-shadow:0 0 3px rgba(0,0,0,.2)}
</style>
</head>
<body>
<div class="page">
  <div class="abs topbar"></div>
  <div class="abs social"><span></span><span></span><span></span><span></span></div>
  <div class="abs student">Student Access</div>
  <div class="abs search"><svg width="10" height="10" viewBox="0 0 10 10"><circle cx="4" cy="4" r="3" fill="none" stroke="#222" stroke-width="1.6"/><line x1="6.3" y1="6.3" x2="9" y2="9" stroke="#222" stroke-width="1.6"/></svg></div>

  <div class="abs brandmark"><i></i><b>TRACKLINE SAFETY</b></div>
  <nav class="abs nav main"><span class="on">Home</span><span>Courses</span><span>Our Services</span><span>About us</span><span>Funding</span><span>Locations</span><span>Contact us</span></nav>

  <div class="abs btn month">MONTH<span class="caret"></span></div>
  <h1 class="abs title">NOVEMBER 2019</h1>
  <div class="abs btn today">TODAY</div>
  <div class="abs btn arrows">
    <span><svg width="10" height="16" viewBox="0 0 10 16"><polyline points="8,2 2,8 8,14" fill="none" stroke="#1b1b1b" stroke-width="2"/></svg></span>
    <span><svg width="10" height="16" viewBox="0 0 10 16"><polyline points="2,2 8,8 2,14" fill="none" stroke="#1b1b1b" stroke-width="2"/></svg></span>
  </div>

  <div class="abs btn goto">
    <div class="y">2019<span class="caret"></span></div>
    <div class="m">November<span class="caret"></span></div>
    <div class="g">GOTO MONTH</div>
  </div>

  <div class="abs card"></div>

  <div class="abs mini" style="left:213px;top:345px">
    <div class="lbl">10<br>OCTOBER</div><div class="yr">2019</div>
    <div class="hd"></div><div class="bd"></div>
  </div>
  <div class="monthhead abs">
    <div class="n">11</div>
    <div class="nm">NOVEMBER</div>
    <div class="yr">2019</div>
  </div>
  <div class="abs mini" style="left:572px;top:345px">
    <div class="lbl">12<br>DECEMBER</div><div class="yr">2019</div>
    <div class="hd"></div><div class="bd"></div>
  </div>

  <div class="abs weekdays">
    <span class="we">Sunday</span><span>Monday</span><span>Tuesday</span><span>Wednesday</span><span>Thursday</span><span>Friday</span><span class="we">Saturday</span>
  </div>

  <div class="abs grid">
    <span class="prev">27</span><span class="prev">28</span><span class="prev">29</span><span class="prev">30</span><span class="prev">31</span><span>1 Nov</span><span class="sat">2</span>
    <span>3</span><span class="sel">4</span><span>5</span><span>6</span><span>7</span><span>8</span><span class="sat">9</span>
    <span>10</span><span>11</span><span>12</span><span>13</span><span>14</span><span>15</span><span class="sat">16</span>
    <span>17</span><span>18</span><span>19</span><span>20</span><span>21</span><span>22</span><span class="sat">23</span>
    <span>24</span><span>25</span><span>26</span><span>27</span><span>28</span><span>29</span><span>30</span>
  </div>

  <h2 class="abs dtitle">COURSE DETAILS</h2>
  <div class="abs dline"></div>
  <dl class="abs details">
    <dt>Course Code:</dt><dd>TLILOO05</dd>
    <dt>Course Title:</dt><dd>Basic Scaffolding</dd>
    <dt>Course Date:</dt><dd>Monday, November 04, 2019</dd>
    <dt>Course Time:</dt><dd>8:00:00 AM</dd>
    <dt>Duration:</dt><dd>5 days</dd>
    <dt>Location:</dt><dd>Townsville</dd>
    <dt>Price:</dt><dd>$500</dd>
    <dt>Member Discount Price:</dt><dd>$200</dd>
  </dl>

  <footer class="abs footer"></footer>
  <div class="abs fbrand"><i></i><b>TRACKLINE SAFETY</b></div>
  <div class="abs follow"><em>Follow us on :-</em><span></span><span></span><span></span><span></span></div>
  <nav class="abs nav foot"><span>Home</span><span>Courses</span><span>Our Services</span><span>About us</span><span>Funding</span><span>Locations</span><span>Contact us</span></nav>
  <div class="abs contact c1"><span class="ic"><svg width="10" height="13" viewBox="0 0 10 13"><path d="M5 0a5 5 0 0 0-5 5c0 3.5 5 8 5 8s5-4.5 5-8a5 5 0 0 0-5-5z" fill="#fff"/><circle cx="5" cy="5" r="1.8" fill="#111"/></svg></span>18 Harbour Lane, Northgate QLD 4013</div>
  <div class="abs contact c2"><span class="ic"><svg width="13" height="9" viewBox="0 0 13 9"><rect width="13" height="9" fill="#fff"/><polyline points="0,0 6.5,5 13,0" fill="none" stroke="#111" stroke-width="1.2"/></svg></span>bookings@tracklinesafety.edu.au</div>
  <div class="abs bottombar">© Copyright All Right Reserved | Powered by Trackline Safety.</div>
  <div class="abs totop"><svg width="14" height="9" viewBox="0 0 14 9"><polyline points="1,8 7,2 13,8" fill="none" stroke="#222" stroke-width="2"/></svg></div>
</div>
</body>
</html>
```